Luxury startup skincare company needs packaging design

We want a label design for glass jars and a packaging box. The label design will be unique, clean, classy, and expensive looking. The design must be eye-catching and colorful, bold and universal. I

I've attached the logo variations for your reference. The glass jar will need a label for the top as well as a wrap-around label and the packaging will need to be designed per specs that will be provided. We currently have one product and will be expanding to several once the brand grows.

Target Market(s)

Women with disposable income 25-65 years old who care about their skincare routine

Industry/Entity Type

Beauty

Font styles to use
Decorative

Requirements
Must have
• my logo

```html
<!DOCTYPE html>
<html lang="en">
<head>
<meta charset="UTF-8">
<title>Sable Roots – Repairing Mask Label</title>
<link href="https://fonts.googleapis.com/css2?family=Montserrat:wght@800&family=Raleway:wght@300;500;700&display=swap" rel="stylesheet">
<style>
  :root {
    --page-bg: #eceeef;
    --label-black: #0b0b0c;
    --rose-light: #eeaba4;
    --rose-mid: #d88c86;
    --rose-deep: #c47874;
    --rose-accent: #d9938c;
    --white: #ffffff;
    --ink: #1a1212;
  }
  * { margin: 0; padding: 0; box-sizing: border-box; }
  html, body {
    width: 1106px; height: 1200px; overflow: hidden;
    background: var(--page-bg);
  }
  .canvas { position: relative; width: 1106px; height: 1200px; }
  .wrap-label {
    position: absolute; left: 33px; top: 406px;
    width: 1330px; height: 495px;
    transform: scale(0.782); transform-origin: 0 0;
    font-family: "Raleway", sans-serif;
    background: var(--label-black);
    overflow: hidden;
  }
  .rose-panel {
    position: absolute; left: 0; top: 0; width: 510px; height: 495px;
    background: linear-gradient(90deg, var(--rose-mid) 0%, var(--rose-light) 45%, var(--rose-deep) 100%);
  }
  .copy-left {
    position: absolute; left: 50px; top: 32px; width: 275px;
    font-size: 13.5px; line-height: 16.4px; font-weight: 500;
    color: var(--ink); text-align: center;
  }
  .copy-left p + p { margin-top: 14px; }
  .info-box {
    position: absolute; left: 88px; top: 358px; width: 193px; height: 103px;
    background: var(--white);
  }
  .brand-mark {
    position: absolute; left: 495px; top: 76px; width: 26px; height: 26px;
    border-radius: 50%; background: var(--rose-accent);
  }
  .brand-name {
    position: absolute; left: 567px; top: 66px;
    font-weight: 300; color: var(--white); line-height: 1;
  }
  .brand-name .line-1 { display: block; font-size: 34px; letter-spacing: 22px; }
  .brand-name .line-2 { display: block; font-size: 18px; letter-spacing: 20px; margin-top: 14px; }
  .product-title {
    position: absolute; right: 482px; top: 222px;
    font-family: "Montserrat", sans-serif; font-weight: 800;
    font-size: 44px; line-height: 44px; color: var(--white); text-align: right;
  }
  .rule {
    position: absolute; left: 598px; width: 250px; height: 2px;
    background: var(--rose-accent);
  }
  .rule.top { top: 340px; }
  .rule.bottom { top: 388px; }
  .product-claim {
    position: absolute; right: 482px; top: 353px;
    font-weight: 700; font-size: 18px; color: var(--white);
  }
  .product-desc {
    position: absolute; right: 482px; top: 398px;
    font-size: 16.5px; line-height: 20px; font-weight: 500;
    color: var(--white); text-align: right;
  }
  .copy-right {
    position: absolute; left: 925px; top: 57px; width: 362px;
    font-size: 13.5px; line-height: 16.4px; font-weight: 500;
    color: var(--white); text-align: center;
  }
  .copy-right p + p { margin-top: 16px; }
</style>
</head>
<body>
<div class="canvas">
  <div class="wrap-label">
    <div class="rose-panel" role="img" aria-label="Rose-gold decorative wave ribbon area"></div>

    <div class="copy-left">
      <p>Lorem ipsum dolor sit amet, consec&shy;tetuer adipiscing elit, sed diam nonummy nibh euismod tincidunt ut laoreet dolore magna aliquam erat volutpat. Ut wisi enim ad minim veniam, quis nostrud exerci tation ullamcorper suscipit lobortis nisl ut aliquip ex ea commodo consequat. Duis autem vel eum iriure dolor in hendrerit in vulputate velit esse molestie consequat, vel illum dolore eu</p>
      <p>Lorem ipsum dolor sit amet, consec&shy;tetuer adipiscing elit, sed diam nonummy nibh euismod tincidunt ut laoreet dolore magna aliquam erat volutpat. Ut wisi enim ad minim veniam, quis nostrud exerci tation ullamcorper suscipit lobortis nisl ut aliquip ex ea commodo consequat.</p>
    </div>
    <div class="info-box"></div>

    <div class="brand-mark"></div>
    <div class="brand-name">
      <span class="line-1">SABLE</span>
      <span class="line-2">ROOTS</span>
    </div>

    <h1 class="product-title">REPAIRING<br>MASK</h1>
    <div class="rule top"></div>
    <div class="product-claim">INFUSED WITH ARGAN OIL</div>
    <div class="rule bottom"></div>
    <p class="product-desc">Deep moisturization to replenish<br>and help restore hair health</p>

    <div class="copy-right">
      <p>Lorem ipsum dolor sit amet, consectetuer adipiscing elit, sed diam nonummy nibh euismod tincidunt ut laoreet dolore magna aliquam erat volutpat. Ut wisi enim ad minim veniam, quis nostrud exerci tation ullamcorper suscipit lobortis nisl ut aliquip ex ea commodo consequat. Duis autem vel eum iriure dolor in hendrerit in vulputate velit esse molestie consequat,</p>
      <p>Lorem ipsum dolor sit amet, consectetuer adipiscing elit, sed diam nonummy nibh euismod tincidunt ut laoreet dolore magna aliquam erat volutpat. Ut wisi enim ad minim veniam, quis nostrud exerci tation ullamcorper suscipit lobortis nisl ut aliquip ex ea commodo consequat. Duis autem vel eum iriure dolor in hendrerit in vulputate velit esse molestie consequat,</p>
      <p>Lorem ipsum dolor sit amet, consectetuer adipiscing elit, sed diam nonummy nibh euismod tincidunt ut laoreet dolore magna aliquam erat volutpat. Ut wisi enim ad minim veniam, quis nostrud exerci tation ullamcorper suscipit lobortis nisl ut aliquip ex ea commodo consequat. Duis autem vel eum iriure dolor in hendrerit in vulputate velit esse molestie consequat,</p>
    </div>
  </div>
</div>
</body>
</html>
```